new customer flyer 8.5 X 11 to get people who use CPAP, Snore or have sleep apnea to call us

We sell CPAP equipment and supplies in Ontario. We are designing a flyer for a an advertising campaign encouraging people to switch from the current CPAP supplier to us. Our company name is Breathwell Depot. We are different from a typical CPAP supply store in many ways. A typical store is open 9-5 monday-friday, and the customer must come to the store to get any service. We offer free delivery of supplies of the customer is using the same supplies, so they can just have their supplies shipped rather than come in to pick them up. We also offer free home visits where we will do all the services that can be done in store, including determine the best machine they need, fit them for a mask, set up their equipment and supplies, offer advice, and much more. We also offer night and weekend appointments. Finally we will buy used equipment from our customers and donate this equipment to those in the community who may not be able to afford new equipment, which has 2 benefits of reducing waste and helping the needy.

If you can come up with any other concepts to make us stand out we are open to this.

Our flyer needs to offer a call to action of providing a Prixa Gift card to new customers plus additional call to actions if you are able to create one based on info herein. The gift card amount is $50.00 if this is relevant. We can limit the number available for the promotion if you feel it would encourage a faster and quicker response rate.

The Info needed in the flyer is:
1) Company Name: Breathwell Depot
2) Phone number: 289-517-3064
3) website: www.breathwelldepot-example.com (Make creative in a way that it is easy for user to determine what it says and stimulate them to remember it.)
4) Address is optional, which is 418 Marlow Street, Fort Erie ON L2A 7K3
5) We cover the entire Niagara region and Region of Hamilton in Ontario Canada
6) A call to action is a MUST. We were thinking of using a $50 Prixa gift card for new customers or something else if you feel it would drive more calls to us or more website visits.
7) The objective is to get the customer to call us so we can make them a new customer. The secondary objective is to get the customer to visit our website, because even if they are hesitant to call us, we hope to get them to visit our website and this will give them the confidence to call us.
8) The call to action must encourage a response to hopefully get a call right away. we don't want the customer putting us on the back burner.
9) The flyer is encouraged to not only get people who have sleep apnea, snoring or are currently on CPAP to call, but to also get people who may not suffer from any of these conditions to want to give the flyer to their friends or family who does.
10) I included a bunch of pictures but they are just random pictures, you can use them, use your own or use drawings or whatever to get the message across. You do not need to use all or any of the pictures I provided.
11) We accept all health insurances

I am pretty open, so have fun with the project and be creative as possible!
Updates

There are many designs submitted but many that do not meet the requirements, and many that are similar. I am hoping to find one that does not look like every other generic design, and work with some of the designers who have submitted entries with some potential to modify them into something useable.

Target Market(s)

1) People who snore, have sleep apnea or already use CPAP.
2) Spouses of people snore or have sleep apnea, as these people notice the person who is snoring or having erratic breathing.
3) Friends or family of the people above so that they share the flyer.
4) Focus on 30-60 year old males.

Industry/Entity Type

Advertising

Colors

Designer to choose colors to be used in the design.

Requirements
Must have
• 1) Company Name: Breathwell Depot (Logo can serve as company name as well, files attached)
• 2) Phone number: 289-517-3064
• 3) website: www.breathwelldepot-example.com (Make creative in a way that it is easy for user to determine what it says and stimulate them to remember it.)
• 4) Flyer needs to be friendly and engaging.
• 5) Flyer can be funny or humorous if it will generate customers.
• 6) A call to action is a MUST. We were thinking of using a $50 Prixa gift card for new customers or something else if you feel it would drive more calls to us or more website visits.
• 7) The objective is to get the customer to call us so we can make them a new customer. The secondary objective is to get the customer to visit our website, because even if they are hesitant to call us, we hope to get them to visit our website and this will give them the confidence to call us.
• 8) The call to action must encourage a response to hopefully get a call right away. we don't want the customer putting us on the back burner.
• 9) The flyer is encouraged to not only get people who have sleep apnea, snoring or are currently on CPAP to call, but to also get people who may not suffer from any of these conditions to want to give the flyer to their friends or family who does.
• 10) I included a bunch of pictures but they are just random pictures, you can use them, use your own or use drawings or whatever to get the message across. You do not need to use all or any of the pictures I provided.
• 11) We accept all health insurances
• 12) The FLYER MUST be bold and stand out. This can be with full color, unique text or graphics, or colored backgrounds (Including really bold colors). The point is there is really not a defined market to target with this industry, so any flyers are random location flyers that must be so bold as to grab someones attention such that they want to see what the flyer says.
• 13) Because CPAP only affects about 10-15% of the population, the flyer should be designed that those who snore, suffer from sleep apnea, or CURRENTLY USE CPAP will immediately relate to the flyer and as such want to read it and hopefully call us.
Nice to have
• 1) Address is optional, which is 418 Marlow Street, Fort Erie ON L2A 7K3 (We encourage people to let us come to them, because we offer free shipping and home visits. Therefore our address is not really terribly important.
• 2) We cover the entire Niagara region and Region of Hamilton in Ontario Canada. If they get our flyer they hopefully will call us, however if this can be fit in it confirms that we service the customers area. Without it the customer may wonder if we go to the area where they live.
• 3) Our Taglines are "We make CPAP Personal" and "Better sleep for better health", if they fit into the theme of the designed flyer feel free to add one or both of these.
• 4) The flyer can be designed to appear medical in design if this works, but I prefer fun, engaging and even humorous first, and the medical part becomes secondayry.
Should not have
• 1) The flyer can not be scary or make someone feel uncomfortable.

```html
<!DOCTYPE html>
<html lang="en">
<head>
<meta charset="utf-8">
<title>Breathwell Depot – New Customer Flyer</title>
<link rel="stylesheet" href="https://fonts.googleapis.com/css2?family=Lato:wght@400;700&family=Montserrat:wght@700&family=Great+Vibes&family=Oswald:wght@500&display=swap">
<style>
  :root {
    --purple: #8e3f9e;
    --green: #16ad6b;
    --ink: #3c3c3c;
    --backdrop: #e9e6e2;
    --white: #ffffff;
  }
  * { box-sizing: border-box; margin: 0; padding: 0; }
  html, body { width: 1200px; height: 1200px; overflow: hidden; }
  body { background: var(--backdrop); font-family: "Lato", sans-serif; color: var(--ink); }
  .flyer {
    position: absolute; left: 190px; top: 20px; width: 820px; height: 1160px;
    background: var(--white); overflow: hidden;
    box-shadow: 0 4px 18px rgba(0,0,0,.15);
  }
  .hero-photo {
    position: absolute; left: 0; top: 140px; width: 820px; height: 430px;
    background: linear-gradient(180deg, #f4f4f4 0%, #ece7df 40%, #e8e9ef 100%);
  }
  .shapes { position: absolute; inset: 0; }
  .brand {
    position: absolute; left: 48px; top: 88px; display: flex; align-items: center; gap: 10px;
    white-space: nowrap;
  }
  .brand-dot { width: 20px; height: 20px; border-radius: 50%; background: var(--purple); }
  .brand-name { font-family: "Lato", sans-serif; font-weight: 400; font-size: 28px; color: var(--green); }
  .taglines {
    position: absolute; right: 50px; top: 56px; text-align: right;
    font-family: "Montserrat", sans-serif; font-weight: 700; white-space: nowrap;
  }
  .tagline-main { font-size: 29px; color: var(--purple); line-height: 1.15; }
  .tagline-sub { font-size: 21px; color: var(--green); line-height: 1.35; }

  .gift-card {
    position: absolute; left: 67px; top: 518px; width: 283px; height: 138px;
    background: linear-gradient(135deg, #fbfaf7, #eeeae4);
    border: 1px solid #cfcfcf; outline: 3px solid #fff; box-shadow: 0 2px 6px rgba(0,0,0,.2);
  }
  .gift-ribbon {
    position: absolute; left: 8px; top: 0; width: 86px; height: 136px;
    background: linear-gradient(90deg, rgba(142,63,158,0) 0%, #9a45aa 30%, #8b2f99 70%, rgba(142,63,158,0) 100%);
  }
  .gift-text { position: absolute; left: 100px; right: 8px; top: 20px; text-align: center; white-space: nowrap; }
  .gift-get { font-family: "Great Vibes", cursive; font-size: 34px; color: var(--green); line-height: 1; }
  .gift-amount { font-family: "Oswald", sans-serif; font-weight: 500; font-size: 25px; color: var(--purple); line-height: 1.3; }
  .gift-note { font-size: 11.5px; color: var(--green); }

  .story { position: absolute; left: 48px; top: 700px; width: 314px; }
  .story h2 { font-family: "Lato", sans-serif; font-weight: 700; font-size: 19px; color: var(--purple); margin-bottom: 10px; }
  .story-rule { position: absolute; left: 48px; top: 683px; width: 314px; border-top: 1px solid #cfcfcf; }
  .story p { font-size: 11.6px; line-height: 15px; text-align: justify; margin-bottom: 14px; }
  .insurance {
    position: absolute; left: 48px; top: 1026px; display: flex; align-items: center; gap: 8px;
    font-size: 20px; color: var(--green); white-space: nowrap;
  }

  .offer { position: absolute; left: 422px; top: 700px; width: 350px; }
  .offer-title { display: flex; align-items: center; gap: 8px; margin-bottom: 12px; }
  .offer-title h2 { font-family: "Montserrat", sans-serif; font-weight: 700; font-size: 23px; color: var(--purple); letter-spacing: .5px; }
  .offer-title span { flex: 1; border-top: 1px solid #cfcfcf; margin-top: 6px; }
  .offer-item { display: flex; gap: 10px; margin-bottom: 13px; }
  .offer-item svg { flex: none; width: 26px; height: 20px; margin-top: 1px; }
  .offer-item p { font-size: 11.6px; line-height: 15px; text-align: justify; }
  .offer-item b { color: var(--green); font-weight: 700; }

  .footer-bar { position: absolute; left: 0; top: 1114px; width: 820px; height: 34px; background: var(--green); }
  .footer-line { position: absolute; left: 0; top: 1150px; width: 820px; height: 10px; background: var(--purple); }
  .footer-item {
    position: absolute; top: 1122px; display: flex; align-items: center; gap: 7px;
    color: #fff; font-size: 12.5px; font-weight: 700; white-space: nowrap;
  }
  .footer-address { left: 40px; }
  .footer-web { left: 318px; }
  .footer-phone {
    position: absolute; right: 40px; top: 1113px; display: flex; align-items: center; gap: 8px;
    color: #fff; font-size: 22px; font-weight: 700; white-space: nowrap;
  }
</style>
</head>
<body>
<main class="flyer">
  <div class="hero-photo" role="img" aria-label="Photo of a smiling couple in bed, the man sleeping comfortably with a CPAP nasal mask"></div>

  <svg class="shapes" viewBox="0 0 820 1160" width="820" height="1160" aria-hidden="true">
    <defs>
      <linearGradient id="panelFade" x1="0" y1="0" x2="0" y2="1">
        <stop offset="0" stop-color="#f6f6f6"/>
        <stop offset="1" stop-color="#e6e6e6"/>
      </linearGradient>
      <radialGradient id="portraitTone" cx="50%" cy="45%" r="60%">
        <stop offset="0" stop-color="#e9d3c6"/>
        <stop offset="1" stop-color="#cfd5de"/>
      </radialGradient>
    </defs>
    <path d="M0,470 C180,400 340,420 500,500 C580,540 700,560 820,500 L820,1160 L0,1160 Z" fill="#fff"/>
    <path d="M0,470 L395,470 L395,1042 Q395,1072 365,1072 L0,1072 Z" fill="url(#panelFade)"/>
    <path d="M0,445 C180,375 340,395 500,478 C580,520 700,540 820,480" fill="none" stroke="var(--purple)" stroke-width="10"/>
    <path d="M0,470 C180,400 340,420 500,500 C580,540 700,560 820,500" fill="none" stroke="var(--green)" stroke-width="22"/>
    <circle cx="633" cy="566" r="112" fill="#fff" stroke="var(--green)" stroke-width="6"/>
    <circle cx="633" cy="566" r="100" fill="url(#portraitTone)" stroke="var(--purple)" stroke-width="1.5" role="img" aria-label="Portrait of a man sleeping with a full-face CPAP mask"/>
    <path d="M612,1104 L820,1104 L820,1160 L584,1160 Z" fill="var(--purple)"/>
  </svg>

  <div class="brand">
    <span class="brand-dot"></span>
    <span class="brand-name">Breathwell Depot</span>
  </div>

  <div class="taglines">
    <div class="tagline-main">We make CPAP Personal</div>
    <div class="tagline-sub">and Better sleep for better health</div>
  </div>

  <div class="gift-card">
    <div class="gift-ribbon" role="img" aria-label="Purple satin gift bow and ribbon"></div>
    <div class="gift-text">
      <div class="gift-get">Get a</div>
      <div class="gift-amount">$50 GIFT CARD</div>
      <div class="gift-note">for becoming a new customer</div>
    </div>
  </div>

  <div class="story-rule"></div>
  <section class="story">
    <h2>Our Story</h2>
    <p>I have sleep apnea and use CPAP just like you. I work really hard every day to provide for my family, and the last thing I want to do on my time off is run errands, including picking up my CPAP supplies. When I searched for a company that put the customer first, that put service before profits, and that went to the customer instead of making the customer come to them, I came up empty.</p>
    <p>Because I'm a paramedic, and naturally care about people, I felt sad for the people who cannot easily visit their local CPAP suppliers (such as the elderly and the disabled) and determined that the best way to help these people was to open up a sleep therapy store that puts the customer first.</p>
    <p>We believe in helping people, and this should always be first. If you treat your customer right, you will always have customers, and these customers become your friends. When you treat people right, they make your life better.</p>
  </section>

  <div class="insurance">
    <svg width="30" height="26" viewBox="0 0 30 26" aria-hidden="true">
      <path d="M15 25 C5 17 1 12 1 7.5 A6.5 6.5 0 0 1 15 5 A6.5 6.5 0 0 1 29 7.5 C29 12 25 17 15 25 Z" fill="var(--purple)"/>
      <path d="M13 9h4v4h4v4h-4v4h-4v-4H9v-4h4z" fill="#fff"/>
    </svg>
    <span>We accept all health insurances.</span>
  </div>

  <section class="offer">
    <div class="offer-title"><h2>WE OFFER</h2><span></span></div>

    <div class="offer-item">
      <svg viewBox="0 0 26 20" aria-hidden="true"><rect x="1" y="4" width="15" height="10" fill="none" stroke="var(--purple)" stroke-width="1.5"/><path d="M16 7h5l4 4v3h-9z" fill="none" stroke="var(--purple)" stroke-width="1.5"/><circle cx="6" cy="16" r="2" fill="var(--purple)"/><circle cx="20" cy="16" r="2" fill="var(--purple)"/></svg>
      <p><b>FREE DELIVERY:</b> So you can spend your time off doing the things you love.</p>
    </div>
    <div class="offer-item">
      <svg viewBox="0 0 26 20" aria-hidden="true"><path d="M2 10 L13 2 L24 10 H21 V18 H5 V10 Z" fill="var(--purple)"/><rect x="11" y="12" width="4" height="6" fill="#fff"/></svg>
      <p><b>FREE HOME VISITS:</b> Because we don't just want to sell you supplies, we want to set them up for you, make sure all your questions are answered, and make sure you get everything you need.</p>
    </div>
    <div class="offer-item">
      <svg viewBox="0 0 26 20" aria-hidden="true"><rect x="2" y="2" width="18" height="16" fill="none" stroke="var(--purple)" stroke-width="1.5"/><path d="M2 6h18M6 10h3M11 10h3M6 14h3M11 14h3" stroke="var(--purple)" stroke-width="1.5"/><path d="M20 14h5M22.5 11.5v5" stroke="var(--purple)" stroke-width="1.5"/></svg>
      <p><b>NIGHT AND WEEKEND APPOINTMENTS:</b> Not everyone works 9-5 Monday through Friday. We offer night and weekend appointments to make sure you can get the service you need on your schedule.</p>
    </div>
    <div class="offer-item">
      <svg viewBox="0 0 26 20" aria-hidden="true"><path d="M1 2h4l3 11h13l3-8H7" fill="none" stroke="var(--purple)" stroke-width="1.6"/><circle cx="10" cy="17" r="1.8" fill="var(--purple)"/><circle cx="19" cy="17" r="1.8" fill="var(--purple)"/></svg>
      <p><b>WE BUY YOUR OLD SUPPLIES :</b> There are many people who can't afford their supplies, but we want to help them however we can. So part of our commitment to serving everyone is that we buy your gently used equipment, refurbish what we can, and donate it to those who need it.</p>
    </div>
    <div class="offer-item">
      <svg viewBox="0 0 26 20" aria-hidden="true"><circle cx="13" cy="6" r="4.5" fill="none" stroke="var(--purple)" stroke-width="1.5"/><path d="M4 19 Q4 11 13 11 Q22 11 22 19 Z" fill="none" stroke="var(--purple)" stroke-width="1.5"/></svg>
      <p><b>PLUS SO MUCH MORE:</b> Call us at <strong>289-517-3064</strong> to speak to a sleep expert who can finally treat you the way you deserve to be treated.</p>
    </div>
  </section>

  <div class="footer-bar"></div>
  <div class="footer-line"></div>
  <div class="footer-item footer-address">
    <svg width="15" height="13" viewBox="0 0 16 14" aria-hidden="true"><path d="M1 7 L8 1 L15 7 H13 V13 H3 V7 Z" fill="#fff"/></svg>
    <span>418 Marlow Street, Fort Erie ON L2A 7K3</span>
  </div>
  <div class="footer-item footer-web">
    <svg width="16" height="16" viewBox="0 0 18 18" aria-hidden="true"><circle cx="9" cy="9" r="7.5" fill="none" stroke="#fff" stroke-width="1.5"/><ellipse cx="9" cy="9" rx="3.2" ry="7.5" fill="none" stroke="#fff" stroke-width="1.3"/><path d="M1.5 9h15" stroke="#fff" stroke-width="1.3"/></svg>
    <span>www.breathwelldepot-example.com</span>
  </div>
  <div class="footer-phone">
    <svg width="18" height="18" viewBox="0 0 20 20" aria-hidden="true"><path d="M5 2 L8 6 L6.5 8 Q8.5 12 12 13.5 L14 12 L18 15 L16 18 Q6 17 2 4 Z" fill="#fff"/></svg>
    <span>289-517-3064</span>
  </div>
</main>
</body>
</html>
```